Pediatric Therapy Clinic Brochure

We need a Brochure for a new pediatric therapy clinic. The clinic offers occupational therapy, physical therapy, speech therapy and feeding therapy. We want a brochure for parents, doctors and medical professional. It should have a fun and inviting, but still professional feel. Should be kid focused, bright and colorful. All the text / wording is there and a rough layout. Now I need someone to tidy and jazz it up and make it look professional.

Target Market(s)

Parents, doctors, medical professional

Industry/Entity Type

Medical

Font styles to use
Serif
Sans Serif

Requirements
Must have
• Keep All the text with information about services the same. Logo on front. Pictures throughout (use any of the pictures provided) (try and match up with corresponding service) (pictures are labeled). Need to have Map and contact info
• Keep colors consistent with our logo
Nice to have
• Background, special effects. Make it look fancy and professional
Should not have
• Not so busy that is takes away from the text

```html
<!DOCTYPE html>
<html lang="en">
<head>
<meta charset="utf-8">
<title>Pediatric Therapy Clinic Brochure – Services Spread</title>
<link href="https://fonts.googleapis.com/css2?family=Montserrat:wght@800&family=Open+Sans:ital,wght@0,400;0,600;1,400&display=swap" rel="stylesheet">
<style>
  :root{
    --backdrop:#9c9c9c;
    --paper:#ffffff;
    --sky:#2f86c8;
    --sky-soft:#cfe4f4;
    --orange:#ee6a1e;
    --orange-soft:#fbd3b6;
    --ink-blue:#1e5f9c;
    --heading:"Montserrat", Arial, sans-serif;
    --body:"Open Sans", Arial, sans-serif;
  }
  *{box-sizing:border-box;margin:0;padding:0}
  html,body{width:1200px;height:1200px;overflow:hidden;background:var(--backdrop)}
  .spread{
    position:absolute;left:40px;top:340px;width:1120px;height:520px;
    display:flex;box-shadow:0 18px 40px rgba(0,0,0,.35);
  }
  .page{
    position:relative;width:560px;height:520px;overflow:hidden;
    background:
      linear-gradient(to bottom,var(--sky) 0,var(--sky-soft) 42px,var(--paper) 90px,var(--paper) 400px,var(--orange-soft) 470px,var(--orange) 520px);
  }
  .page--left::after{
    content:"";position:absolute;right:0;top:0;width:40px;height:100%;
    background:linear-gradient(to right,rgba(0,0,0,0),rgba(0,0,0,.12));
  }
  .page--right::before{
    content:"";position:absolute;left:0;top:0;width:40px;height:100%;
    background:linear-gradient(to left,rgba(0,0,0,0),rgba(0,0,0,.12));
  }
  .service{position:absolute;z-index:2;color:var(--ink-blue);font-family:var(--body);font-size:10px;line-height:13px}
  .service__title{
    font-family:var(--heading);font-weight:800;font-variant:small-caps;
    color:var(--orange);font-size:15px;letter-spacing:.5px;line-height:17px;
  }
  .service__tagline{
    font-family:var(--body);font-weight:600;font-variant:small-caps;text-transform:lowercase;
    color:var(--orange);font-size:11.5px;line-height:13px;letter-spacing:.4px;margin-bottom:2px;
  }
  .service__tagline::first-letter{text-transform:uppercase}
  .service ul{list-style:none}
  .service li::before{content:"• "}
  .service__note{font-style:italic;margin-top:4px;font-size:9.5px}
  .inline-title{display:inline}
  .photo{position:absolute;z-index:1}
  .photo--whisper{left:0;top:300px;width:285px;height:190px;
    background:radial-gradient(ellipse at 50% 55%,#e49a6e 0,#d27a3e 35%,rgba(240,150,90,.35) 65%,rgba(255,255,255,0) 80%)}
  .photo--baby{left:448px;top:100px;width:108px;height:175px;
    background:radial-gradient(ellipse at 50% 50%,#e8b49a 0,#8cc56a 35%,#b27a46 55%,rgba(255,255,255,0) 75%)}
  .photo--paint{left:265px;top:290px;width:295px;height:230px;
    background:radial-gradient(ellipse at 50% 45%,#f2c9a8 0,#e0a070 25%,#3a9ad8 45%,#f2c030 58%,rgba(238,106,30,.3) 75%,rgba(255,255,255,0) 90%)}
</style>
</head>
<body>
<main class="spread">
  <section class="page page--left">
    <article class="service" style="left:32px;top:58px;width:215px">
      <h2 class="service__title">Speech Therapy</h2>
      <p class="service__tagline">Helping children speak, communicate and understand language.</p>
      <ul>
        <li>Expressive and Receptive Language</li>
        <li>Speech and Language Developmental Milestones</li>
        <li>Articulation / Intelligibility</li>
        <li>Speech Fluency</li>
        <li>Pragmatics and Social Skills</li>
        <li>Literacy and Vocabulary</li>
        <li>Apraxia of Speech</li>
        <li>Augmentative and Alternative Communication</li>
        <li>Feeding and Oral Motor</li>
      </ul>
    </article>

    <article class="service" style="left:250px;top:88px;width:195px">
      <h2 class="service__title">Occupational Therapy</h2>
      <p class="service__tagline">Helping children build better self-esteem, confidence and independence in all the things they do.</p>
      <ul>
        <li>Sensory Processing Disorder</li>
        <li>Balance, Coordination, Strength, and Endurance</li>
        <li>Fine Motor and Handwriting</li>
        <li>Visual- Motor Integration</li>
        <li>Play and Social Skills</li>
        <li>Feeding and Oral Motor Skills</li>
        <li>Self-Care</li>
        <li>Academic and Cognitive Skills</li>
        <li>Behavioral Difficulties</li>
        <li>Developmental Delays</li>
      </ul>
    </article>

    <div class="photo photo--baby" role="img" aria-label="Photo of a toddler in a knitted hat eating with a spoon"></div>

    <article class="service" style="left:300px;top:300px;width:220px">
      <h2 class="service__title">Physical Therapy</h2>
      <p class="service__tagline">Helping children move and interact within their environment smoothly and confidently.</p>
      <ul>
        <li>Torticollis</li>
        <li>Walking and Mobility</li>
        <li>Developmental Motor Milestones</li>
        <li>Balance, Coordination, Motor Planning</li>
        <li>Strength, Muscle Tone and Range of Motion</li>
        <li>Sports Injuries</li>
        <li>Toe Walking</li>
        <li>Myofascial Release</li>
        <li>Postural Control and Positioning</li>
      </ul>
    </article>

    <div class="photo photo--whisper" role="img" aria-label="Photo of three children whispering to each other"></div>
  </section>

  <section class="page page--right">
    <article class="service" style="left:40px;top:96px;width:290px">
      <p class="service__tagline"><span class="service__title inline-title">Sensory Integration</span> Gradually increasing play based activities to improve a child's nervous system. Helping children learn to self-regulate their emotions, behaviors and arousal levels.</p>
      <ul>
        <li>Autism and ADHD</li>
        <li>Sensory Processing Disorder</li>
        <li>Poor Tolerance of Sensory Stimuli from the Environment</li>
        <li>Meltdowns and Tantrums</li>
        <li>Poor Balance/Body Awareness</li>
        <li>Poor Attention and Concentration</li>
        <li>Poor Self-Regulation</li>
        <li>Behavior and Social Difficulties</li>
        <li>Poor Motor Coordination and Motor Planning</li>
        <li>Aggression, Frustration or Avoidance Behaviors</li>
      </ul>
    </article>

    <article class="service" style="left:350px;top:120px;width:190px">
      <h2 class="service__title">Group Therapy</h2>
      <p class="service__tagline">Using peer role models to learn new and challenging skills.</p>
      <ul>
        <li>Social Groups</li>
        <li>Feeding Groups</li>
      </ul>
      <p class="service__note">**More Group Classes Coming Soon</p>
    </article>

    <article class="service" style="left:40px;top:340px;width:215px">
      <h2 class="service__title">Feeding Therapy</h2>
      <p class="service__tagline">Providing skilled assessment and intervention to children with feeding difficulties.</p>
      <ul>
        <li>Food Aversions</li>
        <li>Food Refusal</li>
        <li>Very Picky Eating</li>
        <li>Avoidance of Certain Textures</li>
        <li>Gagging and Vomiting</li>
        <li>Oral Motor/ Chewing Difficulties</li>
        <li>Limited Diet/Food Repertoire</li>
      </ul>
    </article>

    <div class="photo photo--paint" role="img" aria-label="Photo of a girl framing her eye with colourful paint-covered hands"></div>
  </section>
</main>
</body>
</html>
```